Teodor Ravik, MD Print Package_Trifold

Need a trifold brochure designed. The business is a cosmetic surgery office with cosmetic procedures involving face surgery, body surgery, breast surgery, and skin care treatments. At this point, we would like to see a brochure with some more white space.

A little bit about the doctor for character reference:
Dr. Teodor Ravik believes the art of cosmetic surgery is in listening to his patients. He builds each treatment plan on a solid foundation of communication between doctor and patient and spends a considerable amount of time getting to know the people he treats — taking their goals into account and offering the best options to meet those goals. At our state-of-the-art Bayfield Aesthetic Institute, you are not just a patient; You are our guest.

Their website for further information and for color scheme reference, as the client would like the brochure to match his website (ie: ocean blue/teal, grays and black), is http://www.drtravensolo.example/

Attached is a brochure that the client created a few months back. This shows a general idea of how he would like the layout to be and the information to put on the trifold.

Also Attached are two additional Before & Afters for the brochure, per the client's request. As well as a picture of the Vexa Beam machine that performs these procedures.

Also attached is a brochure intake document for further guidelines as well.
Updates

Industry/Entity Type

Business

Requirements
Must have
• If utilizing any staff photos - please be sure to use Dr. Teodor Ravik, you can find him here:
• http://www.drtravensolo.example/about

```html
<!DOCTYPE html>
<html lang="en">
<head>
<meta charset="utf-8">
<title>Teodor Ravik, MD – Trifold Brochure</title>
<link href="https://fonts.googleapis.com/css2?family=Open+Sans:ital,wght@0,300;0,400;0,600;0,700;1,400;1,600;1,800&display=swap" rel="stylesheet">
<style>
:root{
  --stage:#e9edef;
  --slate:#4d7180;
  --slate-dark:#3e5f6d;
  --slate-light:#a8c2cb;
  --mist:#dfe7ea;
  --ink:#2b4450;
  --text:#3d3d3d;
  --white:#ffffff;
  --sky:#7fc3dc;
}
*{box-sizing:border-box;margin:0;padding:0}
html,body{width:762px;height:1200px;overflow:hidden}
body{background:var(--stage);font-family:"Open Sans",Arial,sans-serif;position:relative;color:var(--text)}
.sheet-label{position:absolute;left:0;width:762px;text-align:center;font-weight:800;font-style:italic;font-size:25px;color:#111;letter-spacing:.5px}
.sheet{position:absolute;left:47px;width:670px;overflow:hidden;box-shadow:0 4px 10px rgba(0,0,0,.25);background:var(--white)}
.sheet.outside{top:62px;height:516px}
.sheet.inside{top:645px;height:520px}
.panel{position:absolute;top:0;height:100%}
.p1{left:0;width:223px}.p2{left:223px;width:220px}.p3{left:443px;width:227px}
.waves{position:absolute;left:0;top:0;width:100%;height:100%}
.ba{position:absolute;display:flex;justify-content:space-between}
.ba span{display:block;width:58px;height:13px;background:var(--slate);color:#fff;font-size:8px;line-height:13px;text-align:center}
.ba.light span{background:#fff;color:var(--slate)}
.photo{position:absolute;border-radius:10px;overflow:hidden}
.photo.skin{background:linear-gradient(90deg,#b98a6e,#d3ab90 50%,#c89c80)}
.photo.body{background:linear-gradient(90deg,#2a2220,#c99479 30%,#d9a88c 70%,#1f1a18)}
.photo.dark-skin{background:linear-gradient(90deg,#6d4a35,#8e6248 50%,#6a4733)}
.photo.belly{background:linear-gradient(90deg,#c2a18d,#d7bcab 50%,#cfb19e)}
.photo.scar{background:linear-gradient(90deg,#c27f6d,#d7a291 50%,#dcae9d)}
.photo.tattoo{background:linear-gradient(90deg,#7f8a74,#c79c86 40%,#d8b4a0)}
.photo.cheek{background:linear-gradient(90deg,#c56d66,#d99a8e 50%,#e4b6a8)}
.photo.face-pale{background:linear-gradient(90deg,#d9a190,#e8c2b2 50%,#eccab9)}
.h{position:absolute;font-weight:700;font-style:italic;font-size:9px;color:var(--ink);letter-spacing:.2px}
.h.white{color:#fff}
.copy{position:absolute;font-size:6.9px;line-height:10.5px;text-align:justify}
.copy.white{color:#fff}
.url{position:absolute;font-size:8px;display:flex;align-items:center;gap:4px}
.url i{width:8px;height:8px;border-radius:50%;border:1px solid currentColor;display:block}
.portrait{position:absolute;left:49px;top:38px;width:122px;height:122px;border-radius:50%;background:var(--slate);padding:7px}
.portrait div{width:100%;height:100%;border-radius:50%;background:radial-gradient(circle at 50% 45%,#c98d6c,#7a5240 60%,#3d5c78)}
.doc-name{position:absolute;left:0;width:220px;top:196px;text-align:center;font-size:14px;font-weight:400;color:#333;letter-spacing:.3px}
.chev{position:absolute;left:103px;top:236px}
.bio{position:absolute;left:20px;top:300px;width:180px;color:#fff;font-style:italic;font-size:7.5px;line-height:12.6px;text-align:justify}
.connect{position:absolute;left:100px;top:482px;width:110px;text-align:center;color:#fff;font-size:7px;font-style:italic}
.brand-bar{position:absolute;left:0;top:0;width:227px;height:56px;background:var(--slate)}
.brand{position:absolute;left:18px;top:12px;color:#fff;font-size:10px;font-weight:400;line-height:14px}
.brand small{display:block;font-size:7px;letter-spacing:.5px}
.hero{position:absolute;left:0;top:56px;width:227px;height:178px;background:linear-gradient(90deg,#e6eef1,#f2f6f7 40%,#dbe7eb)}
.hero-title{position:absolute;right:14px;top:94px;text-align:right;font-weight:300;font-size:15px;line-height:21px;color:var(--slate);letter-spacing:.5px}
.services{position:absolute;left:0;width:227px;top:244px;text-align:center;color:#fff}
.services h3{font-size:11px;font-weight:400;font-style:italic;margin-bottom:5px}
.services li{list-style:none;font-size:8.4px;line-height:16.2px}
.phones{position:absolute;right:14px;top:462px;text-align:right;color:#fff}
.phones b{display:block;font-size:11.5px;font-weight:700;line-height:16px}
.phones em{font-size:7px}
.phone-icon{position:absolute;left:188px;top:434px}
.pin{position:absolute;left:101px;top:24px}
.address{position:absolute;left:0;width:220px;top:46px;text-align:center;font-size:6.8px;line-height:10px;color:var(--slate)}
.machine{position:absolute;left:14px;top:10px;width:100px;height:178px;background:linear-gradient(180deg,#eef1f3,#cfd6da 60%,#9aa5ab)}
.machine-title{position:absolute;left:112px;top:82px;font-weight:300;font-size:15px;line-height:21px;color:var(--slate);font-style:italic}
.pill{position:absolute;left:18px;top:480px;background:#fff;border-radius:8px;padding:3px 8px;color:var(--slate)}
</style>
</head>
<body>

<div class="sheet-label" style="top:22px">OUTSIDE PAGE</div>

<section class="sheet outside">
  <div class="panel p1">
    <svg class="waves" viewBox="0 0 223 516" preserveAspectRatio="none" aria-hidden="true">
      <path d="M0 260 C70 240 150 250 223 215 L223 516 L0 516Z" fill="var(--slate-light)"/>
      <path d="M0 270 C80 250 150 260 223 228 L223 516 L0 516Z" fill="var(--slate)"/>
      <path d="M0 470 C80 455 150 470 223 445 L223 516 L0 516Z" fill="#fff"/>
    </svg>
    <div class="ba" style="left:42px;top:35px;width:142px"><span>Before</span><span>After</span></div>
    <div class="photo skin" style="left:15px;top:55px;width:193px;height:78px" role="img" aria-label="Before and after photo of skin around the eyes"></div>
    <div class="h" style="right:15px;top:143px">SKIN REVITALIZATION</div>
    <p class="copy" style="left:15px;top:156px;width:195px">Look as young as you feel with laser revitalization treatment that reduces unwanted signs of aging. Just one laser treatment can diminish the deepest lines without surgery, with minimal downtime, and with long-lasting results. Laser revitalization is great for wrinkles around the eyes, crows feet, lipstick lines, smokers' lines and facial wrinkles.</p>
    <div class="ba light" style="left:42px;top:285px;width:142px"><span>Before</span><span>After</span></div>
    <div class="photo body" style="left:15px;top:303px;width:193px;height:62px" role="img" aria-label="Before and after photo of an abdomen"></div>
    <div class="h white" style="right:15px;top:367px">CRYOCONTOUR</div>
    <p class="copy white" style="left:15px;top:380px;width:195px">The CryoContour procedure is the only FDA-cleared, non-surgical fat reduction treatment that uses controlled cooling to eliminate stubborn fat that resists all efforts through diet and exercise. The results are proven, noticeable, and lasting, so you'll look great from every</p>
    <div class="url" style="left:12px;top:497px;color:#333"><i></i>www.drtravensolo.example</div>
  </div>

  <div class="panel p2" style="background:linear-gradient(90deg,#e4e8ea,#fafafa 30%,#fafafa 70%,#e4e8ea)">
    <svg class="waves" viewBox="0 0 220 516" preserveAspectRatio="none" aria-hidden="true">
      <path d="M0 230 C80 255 150 250 220 215 L220 516 L0 516Z" fill="var(--slate-light)"/>
      <path d="M0 240 C80 262 150 258 220 225 L220 516 L0 516Z" fill="var(--slate)"/>
      <path d="M0 470 C80 480 150 470 220 455 L220 516 L0 516Z" fill="var(--slate-light)"/>
    </svg>
    <div class="portrait"><div role="img" aria-label="Portrait photo of Dr. Teodor Ravik"></div></div>
    <div class="doc-name">TEODOR RAVIK, M.D.</div>
    <svg class="chev" width="14" height="8" viewBox="0 0 14 8" aria-hidden="true"><path d="M1 1 L7 7 L13 1" fill="none" stroke="var(--sky)" stroke-width="2"/></svg>
    <p class="bio">Dr. Teodor Ravik believes the art of cosmetic surgery is in listening to his patients. He builds each treatment plan on a solid foundation of communication between doctor and patient and spends a considerable amount of time getting to know the people he treats — taking their goals into account and offering the best options to meet those goals. At our state-of-the-art Bayfield Aesthetic Institute, you are not just a patient; You are our guest.</p>
    <div class="connect">Connect with us</div>
  </div>

  <div class="panel p3" style="background:var(--slate)">
    <div class="brand-bar"></div>
    <div class="brand">Bayfield Aesthetic Institute<small>TEODOR RAVIK M.D.</small></div>
    <div class="hero" role="img" aria-label="Photo of a woman with smooth skin"></div>
    <div class="hero-title">COSMETIC<br>LASER<br>SERVICES</div>
    <svg class="waves" viewBox="0 0 227 516" preserveAspectRatio="none" aria-hidden="true">
      <path d="M0 236 C80 226 160 236 227 222 L227 240 L0 240Z" fill="var(--slate-light)"/>
      <path d="M0 430 C80 440 150 430 227 410 L227 516 L0 516Z" fill="var(--slate-light)" opacity=".9"/>
    </svg>
    <div class="services">
      <h3>LASER SOLUTIONS FOR</h3>
      <ul>
        <li>· UNWANTED HAIR</li><li>· SUN SPOTS / AGE SPOTS</li><li>· TATTOO REMOVAL</li>
        <li>· ANTI-AGING</li><li>· SURGICAL &amp; ACNE SCARS</li><li>· STRETCH MARKS</li>
        <li>· STUBBORN FAT</li><li>· VESSELS / ROSACEA</li>
      </ul>
    </div>
    <svg class="phone-icon" width="26" height="26" viewBox="0 0 26 26" aria-hidden="true"><circle cx="13" cy="13" r="11.5" fill="none" stroke="#2a3f48" stroke-width="2"/><path d="M9 7 l3 3 -1.5 2 q1.5 3 4 4 l2-1.5 3 3 -2 2 q-6 0 -10.5-10.5Z" fill="#2a3f48"/></svg>
    <div class="phones"><b>BRINMOOR : 555-014-8492</b><b>SALTMERE : 555-019-2125</b><em>Call today to schedule your appointment!</em></div>
  </div>
</section>

<div class="sheet-label" style="top:605px">INSIDE PAGE</div>

<section class="sheet inside">
  <div class="panel p1" style="background:var(--slate)">
    <svg class="waves" viewBox="0 0 223 520" preserveAspectRatio="none" aria-hidden="true">
      <path d="M0 0 H223 V240 C150 255 70 240 0 250Z" fill="#fff"/>
      <path d="M0 250 C70 240 150 255 223 240 V256 C150 268 70 258 0 262Z" fill="var(--slate-light)"/>
    </svg>
    <div class="ba" style="left:42px;top:31px;width:142px"><span>Before</span><span>After</span></div>
    <div class="photo dark-skin" style="left:12px;top:54px;width:197px;height:84px" role="img" aria-label="Before and after photo of skin around the mouth"></div>
    <div class="h" style="left:12px;top:146px">LASER HAIR REMOVAL</div>
    <p class="copy" style="left:12px;top:159px;width:198px">Are you tired of shaving, waxing, tweezing, and plucking? Laser hair removal provides a fast, easy solution for permanent hair reduction, allowing you to look and feel your best without all the hassle. Popular areas for treatment are the lower face, upper lip, underarms, chest, back, bikini and legs. Fees are based on area.</p>
    <div class="ba light" style="left:42px;top:247px;width:142px"><span>Before</span><span>After</span></div>
    <div class="photo belly" style="left:12px;top:267px;width:197px;height:85px" role="img" aria-label="Before and after photo of stretch marks"></div>
    <div class="h white" style="left:12px;top:362px">STRETCH MARKS</div>
    <p class="copy white" style="left:12px;top:375px;width:198px">80% of women and 40% of men have stretch marks. We have the only non-ablative fractional treatment that is FDA approved to minimize the appearance of stretch marks associated with pregnancy, hormonal changes and weight gain. It works by using fractional laser light to break down stretch marks and naturally trigger healthy, new tissue growth, including collagen. Fees are based on the size of the area being treated.</p>
    <div class="pill url"><i></i>www.drtravensolo.example</div>
  </div>

  <div class="panel p2" style="background:linear-gradient(180deg,#fafafa 0,#fafafa 118px,var(--slate-light) 118px)">
    <svg class="pin" width="10" height="13" viewBox="0 0 10 13" aria-hidden="true"><path d="M5 0 a5 5 0 0 1 5 5 c0 3 -5 8 -5 8 s-5-5-5-8 a5 5 0 0 1 5-5Z" fill="var(--slate)"/><circle cx="5" cy="5" r="2" fill="#fafafa"/></svg>
    <p class="address">BAYFIELD AESTHETIC INSTITUTE<br>12 HARBORLINE WAY STE 210, BRINMOOR 00713<br><br>SEAGLASS SKIN STUDIO 4080<br>MARSH ROAD, SALTMERE 00958</p>
    <div class="ba" style="left:43px;top:123px;width:142px"><span>Before</span><span>After</span></div>
    <div class="photo scar" style="left:15px;top:145px;width:192px;height:86px" role="img" aria-label="Before and after photo of a surgical scar"></div>
    <div class="h" style="left:15px;top:244px">SURGICAL &amp; ACNE SCARS</div>
    <p class="copy" style="left:15px;top:257px;width:192px">Imagine yourself with beautiful skin that's free of scars. No more cover-up, extra clothing, or added daily expenses. With laser treatment for scar removal, unwanted scars can be a thing of the past. Laser scar removal is a non-invasive, advanced approach to scar treatment that offers excellent results without the discomfort and downtime of surgery.</p>
    <div class="ba light" style="left:43px;top:332px;width:142px"><span>Before</span><span>After</span></div>
    <div class="photo tattoo" style="left:15px;top:352px;width:192px;height:96px" role="img" aria-label="Before and after photos of tattoo removal"></div>
    <div class="h white" style="left:15px;top:455px">TATTOO REMOVAL</div>
    <p class="copy white" style="left:15px;top:468px;width:192px">Tattoo regret is experienced by many people, due to employment concerns, relationship status, and overall person growth and life changes. Thankfully we obtain state of the art laser technology that</p>
  </div>

  <div class="panel p3" style="background:var(--slate)">
    <svg class="waves" viewBox="0 0 227 520" preserveAspectRatio="none" aria-hidden="true">
      <path d="M0 0 H227 V185 C150 195 70 180 0 192Z" fill="#fff"/>
    </svg>
    <div class="machine" role="img" aria-label="Photo of the Vexa Beam laser machine"></div>
    <div class="machine-title">Vexa Beam<br>Machine</div>
    <div class="ba light" style="left:43px;top:197px;width:142px"><span>Before</span><span>After</span></div>
    <div class="photo cheek" style="left:14px;top:215px;width:200px;height:42px" role="img" aria-label="Before and after photo of rosacea on the cheek"></div>
    <div class="h white" style="left:14px;top:262px">ROSACEA &amp; VESSELS</div>
    <p class="copy white" style="left:14px;top:274px;width:200px">IPL treatment can reduce rosacea redness and "flushing" to reveal clearer, more natural-looking skin in just a few easy treatments, providing a more permanent result than topical creams. Treatment can reduce rash, redness, flushing, acne-like papules, pustules, and patches, inflammation and broken vessels.</p>
    <div class="ba light" style="left:43px;top:348px;width:142px"><span>Before</span><span>After</span></div>
    <div class="photo face-pale" style="left:14px;top:364px;width:200px;height:42px" role="img" aria-label="Before and after photo of facial pigmentation"></div>
    <div class="h white" style="left:14px;top:410px">PIGMENTATION</div>
    <p class="copy white" style="left:14px;top:422px;width:200px">For those of us who've spent too much time in the sun, signs of premature aging may be more prominent than we'd like. Laser treatment can clear away skin discoloration and unwanted pigment to reveal more beautiful skin and give you a more revitalized appearance. Commonly called, Photofacials, this treatment treats age spots, sun damage, birthmarks, melasma and freckles. Fees are based on area treated such as spot treatment or full face treatment.</p>
  </div>
</section>

</body>
</html>
```